Korvex Systems*

Stationary design including business cards, letter heads, envelops and email signatures using our new logo

Target Market(s)

Innovative Technologies

Industry/Entity Type

Defense Contracting

Font styles to use
Sans Serif

```html
<!DOCTYPE html>
<html lang="en">
<head>
<meta charset="utf-8">
<title>Korvex Systems Envelope</title>
<link rel="stylesheet" href="https://fonts.googleapis.com/css2?family=Open+Sans:wght@400;600&display=swap">
<style>
  :root {
    --backdrop: #d9dadc;
    --envelope: #231f20;
    --fold-line: #b9b9bb;
    --ink-light: #ffffff;
  }
  html, body {
    margin: 0;
    padding: 0;
    width: 1200px;
    height: 900px;
    overflow: hidden;
    background: var(--backdrop);
  }
  .envelope-canvas {
    display: block;
    width: 1200px;
    height: 900px;
  }
  .envelope-panel { fill: var(--envelope); }
  .fold-line { fill: none; stroke: var(--fold-line); stroke-width: 1; }
  .brand-name {
    font-family: "Open Sans", sans-serif;
    font-weight: 400;
    font-size: 21px;
    letter-spacing: 0.5px;
    fill: var(--ink-light);
  }
  .return-address {
    font-family: "Open Sans", sans-serif;
    font-weight: 600;
    font-size: 13px;
    fill: var(--ink-light);
  }
  .web-address {
    font-family: "Open Sans", sans-serif;
    font-weight: 600;
    font-size: 12.5px;
    fill: var(--ink-light);
  }
</style>
</head>
<body>
<svg class="envelope-canvas" viewBox="0 0 1240 930" xmlns="http://www.w3.org/2000/svg">
  <rect class="backdrop" width="1240" height="930" fill="var(--backdrop)"/>

  <!-- top flap -->
  <path class="envelope-panel top-flap" d="M236 159 L253 64 Q256 51 270 51 L972 51 Q985 51 988 64 L1005 159 Z"/>
  <!-- side flaps -->
  <path class="envelope-panel side-flap-left" d="M236 159 Q190 172 187 200 L187 524 L236 545 Z"/>
  <path class="envelope-panel side-flap-right" d="M1005 159 Q1051 172 1054 200 L1054 524 L1005 545 Z"/>
  <!-- bottom flap -->
  <path class="envelope-panel bottom-flap" d="M236 545 L243 568 L243 866 Q245 877 257 877 L985 877 Q996 877 998 866 L998 568 L1005 545 Z"/>
  <!-- front panel -->
  <rect class="envelope-panel front-panel" x="236" y="159" width="769" height="386"/>

  <!-- fold lines -->
  <rect class="fold-line" x="236" y="159" width="769" height="386"/>
  <path class="fold-line" d="M247 870 L254 834 Q257 822 272 822 L968 822 Q983 822 986 834 L993 870"/>

  <!-- brand -->
  <text class="brand-name" x="287" y="328">Korvex Systems</text>

  <!-- return address -->
  <text class="return-address" x="288" y="469">
    <tspan x="288" dy="0">48 Ridgeline Avenue</tspan>
    <tspan x="288" dy="18">Northfield, Ohio</tspan>
    <tspan x="288" dy="18">44067</tspan>
  </text>

  <!-- web address on bottom flap, upside down -->
  <text class="web-address" x="620" y="706" text-anchor="middle" transform="rotate(180 620 710)">www.korvexsystems.com</text>
</svg>
</body>
</html>
```